Preferred pricing vendor

We are a plumbing company that has many services
-Boilers & Controls
-Plumbing & Heating
-HVAC & Refrigeration
-Preventative Maintenacne
-Gas fitting & Drain Cleaning

We primarily look after condo buildings, and our preferred service rates ($98, $93, or $88 depending on the contract) extend to all of our clients. So in essence, we look after the mechanical room and common equipment but our clients can call us in for drain cleaning or replacing a fixture in their suite. The discounted rates apply to the personal residence. We want a flyer to let them know they get a discount on our services. A one-pager we can send out to all of our contract clients.

Included source files for our letterhead and logo just so you can see the colours we go with.

Target Market(s)

Residential repairs, individual people, replacement of fixtures in-suite specific repairs

Requirements
Must have
• be colourful and attractive

```html
<!DOCTYPE html>
<html lang="en">
<head>
<meta charset="utf-8">
<title>Keystone Mechanical Inc – Resident Discount Flyer</title>
<link rel="stylesheet" href="https://fonts.googleapis.com/css2?family=Roboto:wght@300;400;500;700;900&display=swap">
<style>
  :root {
    --stage: #8d8d8d;
    --paper: #ffffff;
    --brand-blue: #3a8fcb;
    --brand-orange: #e2673f;
    --photo-light: #b65a43;
    --photo-dark: #4f2a26;
    --ink: #3f3f3f;
    --white: #ffffff;
  }
  * { box-sizing: border-box; margin: 0; padding: 0; }
  html, body { width: 1200px; height: 1082px; overflow: hidden; }
  body {
    background: var(--stage);
    font-family: "Roboto", Arial, sans-serif;
    position: relative;
  }
  .flyer {
    position: absolute;
    left: 232px; top: 21px;
    width: 736px; height: 1040px;
    background: var(--paper);
    box-shadow: 0 6px 18px rgba(0,0,0,.25);
    overflow: hidden;
  }

  /* Brand header */
  .brand {
    position: absolute; top: 34px; left: 0; right: 0;
    display: flex; flex-direction: column; align-items: center; gap: 14px;
  }
  .brand-dot {
    width: 58px; height: 58px; border-radius: 50%;
    background: var(--brand-orange);
  }
  .brand-name {
    font-weight: 900; font-size: 26px; letter-spacing: 1px;
    color: var(--brand-blue); text-transform: uppercase;
  }

  /* Hero */
  .hero {
    position: absolute; left: 88px; top: 161px; width: 562px; height: 311px;
  }
  .hero-photo {
    position: absolute; inset: 0;
    background: linear-gradient(100deg, var(--photo-dark) 0%, var(--photo-light) 45%, #a1503d 75%, #6e3a31 100%);
  }
  .hero-copy {
    position: absolute; left: 0; right: 0; top: 22px;
    text-align: center; color: var(--white);
    padding-left: 18px;
  }
  .hero-lead {
    font-weight: 300; font-size: 24px; letter-spacing: 2px; line-height: 30px;
    text-transform: uppercase;
  }
  .hero-rule {
    width: 70px; height: 4px; background: var(--white);
    margin: 16px auto 20px;
  }
  .hero-title {
    font-weight: 700; font-size: 44px; line-height: 42px;
    text-transform: uppercase; text-shadow: 0 2px 6px rgba(0,0,0,.25);
  }

  /* Services */
  .services {
    position: absolute; left: 0; right: 0; top: 472px; height: 311px;
    background: var(--brand-blue);
  }
  .service {
    position: absolute; width: 170px; margin-left: -85px;
    text-align: center; color: var(--white);
  }
  .service-badge {
    width: 105px; height: 105px; border-radius: 50%;
    background: var(--white); margin: 0 auto;
    display: flex; align-items: center; justify-content: center;
  }
  .service-badge svg { width: 62px; height: 62px; }
  .service-label {
    margin-top: 16px;
    font-weight: 700; font-size: 14.5px; line-height: 22px;
    text-transform: uppercase;
  }

  /* Benefits */
  .benefits {
    position: absolute; left: 0; right: 0; top: 783px; height: 166px;
    background: var(--brand-orange);
  }
  .benefit { position: absolute; top: 48px; display: flex; align-items: center; }
  .benefit-num {
    width: 55px; height: 55px; border-radius: 50%;
    background: var(--white); color: var(--brand-orange);
    display: flex; align-items: center; justify-content: center;
    font-weight: 700; font-size: 20px; flex: none;
  }
  .benefit-text {
    color: var(--white); font-weight: 400; font-size: 13.5px; line-height: 18.5px;
  }
  .benefit--cost .benefit-text { margin-left: 13px; width: 117px; }
  .benefit--portal .benefit-text { margin-left: 16px; width: 150px; }
  .benefit--emergency .benefit-num { margin-top: 10px; }
  .benefit--emergency .benefit-text { margin-left: 16px; width: 172px; }

  /* Contact */
  .contact {
    position: absolute; left: 0; right: 0; top: 970px;
    text-align: center; font-weight: 500; font-size: 14.5px; color: var(--ink);
    word-spacing: 1px;
  }
  .contact .sep { margin: 0 9px; }
</style>
</head>
<body>
  <main class="flyer">
    <header class="brand">
      <span class="brand-dot"></span>
      <span class="brand-name">Keystone Mechanical Inc</span>
    </header>

    <section class="hero">
      <div class="hero-photo" role="img" aria-label="Photo of a technician in a hard hat and safety glasses working on mechanical room equipment, in warm orange tones"></div>
      <div class="hero-copy">
        <p class="hero-lead">Book now<br>to get</p>
        <div class="hero-rule"></div>
        <h1 class="hero-title">Discount<br>Service</h1>
      </div>
    </section>

    <section class="services">
      <div class="service" style="left:196px; top:-51px;">
        <div class="service-badge">
          <svg viewBox="0 0 64 64" fill="none" stroke-linecap="round" stroke-linejoin="round">
            <circle cx="32" cy="32" r="27" stroke="var(--brand-orange)" stroke-width="5"/>
            <path d="M22 42 l8-8 M30 26 l8 8 -6 6 -8-8z" stroke="var(--brand-blue)" stroke-width="4"/>
            <path d="M36 24 l4-4 M40 28 l4-4 M18 46 l4-4" stroke="var(--brand-blue)" stroke-width="4"/>
          </svg>
        </div>
        <p class="service-label">Electrical<br>Service</p>
      </div>
      <div class="service" style="left:367px; top:-51px;">
        <div class="service-badge">
          <svg viewBox="0 0 64 64" fill="none" stroke-linecap="round">
            <circle cx="32" cy="32" r="27" stroke="var(--brand-orange)" stroke-width="5"/>
            <path d="M22 36 c-4-5 2-8 0-14 c5 3 5 9 0 14z M32 36 c-4-5 2-8 0-14 c5 3 5 9 0 14z M42 36 c-4-5 2-8 0-14 c5 3 5 9 0 14z" fill="var(--brand-orange)"/>
            <path d="M18 42 h28" stroke="var(--brand-blue)" stroke-width="5"/>
          </svg>
        </div>
        <p class="service-label">Gas Fitting &amp;<br>Drain Cleaning</p>
      </div>
      <div class="service" style="left:542px; top:-51px;">
        <div class="service-badge">
          <svg viewBox="0 0 64 64" fill="none">
            <circle cx="32" cy="32" r="27" stroke="var(--brand-orange)" stroke-width="5"/>
            <path d="M32 14 c6 10 11 15 11 22 a11 11 0 0 1-22 0 c0-7 5-12 11-22z" fill="var(--brand-blue)"/>
            <path d="M27 36 a5 5 0 0 0 5 5" stroke="var(--white)" stroke-width="3" stroke-linecap="round"/>
          </svg>
        </div>
        <p class="service-label">Plambing<br>Service</p>
      </div>

      <div class="service" style="left:196px; top:124px;">
        <div class="service-badge">
          <svg viewBox="0 0 64 64" fill="none" stroke-linecap="round">
            <circle cx="32" cy="32" r="27" stroke="var(--brand-orange)" stroke-width="5"/>
            <path d="M23 18 c-5 6 5 10 0 16 c-5 6 5 10 0 14 M32 16 c-5 6 5 10 0 16 c-5 6 5 10 0 16 M41 18 c-5 6 5 10 0 16 c-5 6 5 10 0 14" stroke="var(--brand-blue)" stroke-width="3.5"/>
          </svg>
        </div>
        <p class="service-label">Boilers &amp;<br>Controls</p>
      </div>
      <div class="service" style="left:367px; top:124px;">
        <div class="service-badge">
          <svg viewBox="0 0 64 64" fill="none">
            <circle cx="32" cy="32" r="27" stroke="var(--brand-orange)" stroke-width="5"/>
            <path d="M32 13 c3 8 12 12 12 23 a12 12 0 0 1-24 0 c0-6 3-9 5-11 c0 4 2 6 3 6 c-1-7 1-12 4-18z" fill="var(--brand-blue)"/>
            <path d="M32 30 c2 4 6 6 6 10 a6 6 0 0 1-12 0 c0-4 4-6 6-10z" fill="var(--white)"/>
          </svg>
        </div>
        <p class="service-label">Heating<br>Service</p>
      </div>
      <div class="service" style="left:542px; top:124px;">
        <div class="service-badge">
          <svg viewBox="0 0 64 64" fill="none">
            <circle cx="32" cy="32" r="27" stroke="var(--brand-orange)" stroke-width="5"/>
            <g fill="var(--brand-blue)">
              <ellipse cx="32" cy="22" rx="5" ry="9"/>
              <ellipse cx="32" cy="42" rx="5" ry="9"/>
              <ellipse cx="22" cy="32" rx="9" ry="5"/>
              <ellipse cx="42" cy="32" rx="9" ry="5"/>
            </g>
            <circle cx="32" cy="32" r="4" fill="var(--brand-orange)"/>
          </svg>
        </div>
        <p class="service-label">HVAC &amp;<br>Refrigeration</p>
      </div>
    </section>

    <section class="benefits">
      <div class="benefit benefit--cost" style="left:38px;">
        <span class="benefit-num">01</span>
        <p class="benefit-text">Cost-Effective providing one price to complete preventative</p>
      </div>
      <div class="benefit benefit--portal" style="left:244px;">
        <span class="benefit-num">02</span>
        <p class="benefit-text">Portal Access Our advanced client portal allows you to access key information</p>
      </div>
      <div class="benefit benefit--emergency" style="left:474px;">
        <span class="benefit-num">03</span>
        <p class="benefit-text">24-hour emergency services for most of the vital mechanical services in your building.</p>
      </div>
    </section>

    <footer class="contact">
      <span class="sep">|</span>www.keystonemech.ca<span class="sep">|</span>call (403) 555 0148<span class="sep">|</span>help@keystonemech.ca<span class="sep">|</span>
    </footer>
  </main>
</body>
</html>
```